Sales Brochure

We are looking for an 8.5 x 11 folding brochure in a landscape orientation that advertises our product and service offerings. This brochure should have content on both sides.

This brochure would be left at prospect client's business, so it needs to be fresh, professional, and focused.

We have attached two 1-page inserts that we would like you to use for inspiration for the written content in the brochure. We would like the main theme of the brochure to focus on professional, repeatable, and quality IT support for business.

The brochure should have the prospective clients email or call (will provide number and email to winner) to get additional information.

Please be creative with both the content and the design.

Went on vacation/holiday

```html
<!DOCTYPE html>
<html lang="en">
<head>
<meta charset="utf-8">
<title>Nortavex IT Services Brochure</title>
<link href="https://fonts.googleapis.com/css2?family=Montserrat:wght@400;500;600;700&family=Open+Sans:wght@400;600;700&display=swap" rel="stylesheet">
<style>
  :root{
    --backdrop:#e4e4e3;
    --blue:#2a8fd6;
    --blue-light:#4aaae6;
    --navy:#1f2a36;
    --navy-mid:#27343f;
    --ink:#2b3845;
    --grey-text:#5d6670;
    --paper:#f7f8f9;
    --paper-shade:#e9ecee;
    --white:#ffffff;
  }
  *{box-sizing:border-box;margin:0;padding:0}
  html,body{width:1200px;height:2484px;overflow:hidden}
  body{background:var(--backdrop);font-family:'Open Sans',sans-serif;color:var(--ink);position:relative}
  .sheet{position:absolute;overflow:hidden;box-shadow:0 6px 18px rgba(0,0,0,.18)}
  .layer{position:absolute;inset:0}
  .abs{position:absolute}

  /* ---------- front cover ---------- */
  .cover-front{left:120px;top:60px;width:960px;height:742px;background:var(--paper)}
  .brand{font-family:'Montserrat',sans-serif;font-weight:600;letter-spacing:3px;display:flex;align-items:center;gap:12px}
  .brand-dot{width:22px;height:22px;border-radius:50%}
  .cover-front .brand{left:44px;top:54px;color:var(--white);font-size:34px}
  .cover-front .brand-dot{background:var(--white)}
  .headline{left:56px;top:420px;font-family:'Montserrat',sans-serif;font-weight:600;font-size:36px;line-height:1.2;letter-spacing:1px;color:var(--ink)}
  .headline .accent{color:var(--blue)}
  .headline-rule{left:58px;top:564px;width:180px;height:3px;background:var(--blue)}
  .cover-tagline{left:58px;top:584px;font-size:17px;color:var(--grey-text);letter-spacing:.3px}
  .contact-row{display:flex;gap:46px;align-items:center;font-size:14px;color:#c9d2da;letter-spacing:.5px}
  .contact-item{display:flex;align-items:center;gap:8px}
  .contact-icon{width:16px;height:16px}
  .cover-front .contact-row{left:56px;top:686px}

  /* ---------- inside spread ---------- */
  .spread{left:30px;top:920px;width:1140px;height:441px;background:var(--white)}
  .page{position:absolute;top:0;height:441px;width:570px;overflow:hidden}
  .page-left{left:0;background:var(--white)}
  .page-right{left:570px;background:var(--paper)}
  .fold{left:566px;top:0;width:8px;height:441px;background:linear-gradient(90deg,rgba(0,0,0,0),rgba(0,0,0,.12),rgba(0,0,0,0))}

  .services-column{left:0;top:0;width:240px;height:441px;background:var(--navy)}
  .services-title{left:20px;top:26px;font-family:'Montserrat',sans-serif;font-weight:500;font-size:21px;line-height:1.2;color:var(--blue-light)}
  .services-rule{left:20px;top:86px;width:90px;height:2px;background:var(--blue)}
  .services-copy{left:20px;top:98px;width:200px;font-size:8.6px;line-height:1.45;color:#c7d0d8}
  .services-copy p{margin-bottom:7px}
  .services-photo{left:0;top:232px;width:240px;height:209px;background:linear-gradient(135deg,#c9d3dc 0%,#7d8fa0 45%,#2d3b49 100%)}

  .page-left .brand{left:256px;top:22px;font-size:15px;color:var(--navy);letter-spacing:1.5px;gap:6px}
  .page-left .brand-dot{width:11px;height:11px;background:var(--blue)}
  .services-intro{left:256px;top:50px;font-size:9.6px;color:var(--ink)}
  .service-item{left:256px;width:296px;display:flex;gap:10px}
  .service-icon{flex:none;width:30px;height:30px}
  .service-name{font-family:'Montserrat',sans-serif;font-weight:700;font-size:7.4px;color:var(--blue);letter-spacing:.4px;margin-bottom:2px}
  .service-text{font-size:7.4px;line-height:1.4;color:var(--grey-text)}
  .promise-box{left:256px;top:322px;width:296px;height:70px;background:var(--blue);border-radius:4px;padding:9px 11px;font-size:8.4px;line-height:1.5;color:var(--white)}

  .plans-band{left:0;top:0;width:570px;height:178px;background:var(--navy-mid)}
  .plans-title{left:0;top:36px;width:570px;text-align:center;font-family:'Montserrat',sans-serif;font-weight:500;font-size:21px;letter-spacing:.5px;color:var(--blue-light)}
  .plans-intro{left:22px;top:68px;width:526px;font-size:7.6px;line-height:1.45;color:#c7d0d8}
  .plan-card{top:149px;width:156px;height:208px;background:var(--blue);border-radius:5px;padding:36px 10px 10px;color:var(--white);box-shadow:0 3px 6px rgba(0,0,0,.2)}
  .plan-badge{position:absolute;left:58px;top:-21px;width:40px;height:40px}
  .plan-name{font-family:'Montserrat',sans-serif;font-weight:700;font-size:9px;line-height:1.35;text-align:center;letter-spacing:.3px;margin-bottom:8px}
  .plan-text{font-size:6.9px;line-height:1.45;color:#e6f2fb}
  .plan-text p{margin-bottom:5px}
  .rates-note{left:0;top:372px;width:570px;text-align:center;font-size:9px;color:var(--ink)}

  /* ---------- back cover ---------- */
  .cover-back{left:120px;top:1480px;width:960px;height:742px;background:var(--navy)}
  .cover-back .brand{left:0;top:300px;width:960px;justify-content:center;color:var(--white);font-size:46px;letter-spacing:4px}
  .cover-back .brand-dot{width:30px;height:30px;background:var(--white)}
  .back-headline{left:0;top:392px;width:960px;text-align:center;font-family:'Montserrat',sans-serif;font-weight:500;font-size:30px;letter-spacing:1.5px;color:var(--blue)}
  .back-tagline{left:0;top:446px;width:960px;text-align:center;font-size:16px;line-height:1.55;color:#b9c4ce}
  .cover-back .contact-row{left:0;top:560px;width:960px;justify-content:center}
  .back-strip{left:0;top:690px;width:960px;height:52px;background:var(--blue);display:flex;align-items:center;padding-left:56px;font-size:14px;color:var(--white);letter-spacing:.5px}
</style>
</head>
<body>

<!-- FRONT COVER -->
<section class="sheet cover-front" aria-label="Front cover">
  <svg class="layer" width="960" height="742" viewBox="0 0 960 742">
    <defs>
      <linearGradient id="paperFade" x1="0" y1="0" x2="1" y2="1">
        <stop offset="0" stop-color="#ffffff"/>
        <stop offset="1" stop-color="#e3e7ea"/>
      </linearGradient>
      <radialGradient id="techGlow" cx="0.55" cy="0.6" r="0.7">
        <stop offset="0" stop-color="#d9f0ff"/>
        <stop offset="0.25" stop-color="#4b9ccf"/>
        <stop offset="0.6" stop-color="#1d4663"/>
        <stop offset="1" stop-color="#0f1b27"/>
      </radialGradient>
    </defs>
    <rect width="960" height="742" fill="url(#paperFade)"/>
    <polygon points="0,0 430,0 0,470" fill="var(--blue)"/>
    <path d="M410,0 L960,0 L960,355 L300,355 Q262,355 278,318 Z" fill="url(#techGlow)" role="img" aria-label="Photo of a hand holding a glowing laptop surrounded by network and email icons over a world map"/>
    <polygon points="0,660 960,660 960,742 0,742" fill="var(--navy)"/>
    <polygon points="500,646 850,646 850,660 500,660" fill="var(--navy)"/>
    <polygon points="850,630 890,630 920,660 880,660" fill="var(--blue)"/>
  </svg>

  <div class="abs brand"><span class="brand-dot"></span>NORTAVEX</div>

  <h1 class="abs headline">
    <span class="accent">IT STRATEGY</span><br>
    PROCESS IMPROVEMENT<br>
    PROCUREMENT
  </h1>
  <div class="abs headline-rule"></div>
  <p class="abs cover-tagline">NORTAVEX aligns current and emerging technologies with your business.</p>

  <div class="abs contact-row">
    <span class="contact-item">
      <svg class="contact-icon" viewBox="0 0 16 16"><circle cx="8" cy="8" r="7.5" fill="var(--blue)"/><rect x="4" y="5.5" width="8" height="5.5" fill="none" stroke="#fff" stroke-width="1"/><path d="M4 5.5 L8 8.5 L12 5.5" fill="none" stroke="#fff" stroke-width="1"/></svg>
      hello@nortavex.com
    </span>
    <span class="contact-item">
      <svg class="contact-icon" viewBox="0 0 16 16"><circle cx="8" cy="8" r="7.5" fill="var(--blue)"/><path d="M5.5 4.5 L7 4.5 L7.5 6.5 L6.6 7.2 Q7.5 9 8.8 9.4 L9.5 8.5 L11.5 9 L11.5 10.5 Q8 11.5 5.5 7 Z" fill="#fff"/></svg>
      555.210.4471
    </span>
    <span class="contact-item">
      <svg class="contact-icon" viewBox="0 0 16 16"><circle cx="8" cy="8" r="7.5" fill="var(--blue)"/><circle cx="8" cy="8" r="4" fill="none" stroke="#fff" stroke-width="1"/><path d="M4 8 H12 M8 4 Q5.8 8 8 12 M8 4 Q10.2 8 8 12" fill="none" stroke="#fff" stroke-width=".8"/></svg>
      www.nortavex.com
    </span>
  </div>
</section>

<!-- INSIDE SPREAD -->
<section class="sheet spread" aria-label="Inside spread">
  <!-- left page -->
  <div class="page page-left">
    <div class="abs services-column"></div>
    <h2 class="abs services-title">NORTAVEX<br>SERVICES</h2>
    <div class="abs services-rule"></div>
    <div class="abs services-copy">
      <p>We provide responsive, quality IT solutions to Calgary, Airdrie, Three Hills and the surrounding areas.</p>
      <p>Our unique SteadyCARE service plans provide fast response times, and our project services provide expert IT help at an affordable price.</p>
      <p>Professionalism and reliable customer service is our standard.</p>
    </div>
    <div class="abs services-photo" role="img" aria-label="Photo of a person at a desk working with a laptop, tablet and phone"></div>

    <div class="abs brand"><span class="brand-dot"></span>NORTAVEX</div>
    <p class="abs services-intro">Here are a few ways in which we take care of your IT needs:</p>

    <div class="abs service-item" style="top:76px">
      <svg class="service-icon" viewBox="0 0 30 30"><circle cx="15" cy="15" r="14" fill="none" stroke="var(--navy)" stroke-width="1.4"/><rect x="8" y="9" width="14" height="9" fill="none" stroke="var(--blue)" stroke-width="1.4"/><path d="M12 21 H18 M15 18 V21" stroke="var(--blue)" stroke-width="1.4"/></svg>
      <div>
        <div class="service-name">DESKTOP SUPPORT</div>
        <p class="service-text">Our desktop support technicians are on hand around the clock to respond to calls or incidents logged in our ticket system. We start with remote support and come on site when the issue needs it, so every fix is fast and you are kept informed.</p>
      </div>
    </div>
    <div class="abs service-item" style="top:162px">
      <svg class="service-icon" viewBox="0 0 30 30"><circle cx="15" cy="15" r="14" fill="none" stroke="var(--navy)" stroke-width="1.4"/><rect x="8" y="8" width="14" height="10" fill="none" stroke="var(--blue)" stroke-width="1.4"/><circle cx="15" cy="13" r="2.2" fill="var(--blue)"/><path d="M11 22 H19" stroke="var(--blue)" stroke-width="1.4"/></svg>
      <div>
        <div class="service-name">SYSTEMS MANAGEMENT</div>
        <p class="service-text">We put our skill in systems and network technology (email, servers, cloud, wireless, printing and remote access) to work for you.</p>
      </div>
    </div>
    <div class="abs service-item" style="top:212px">
      <svg class="service-icon" viewBox="0 0 30 30"><circle cx="15" cy="15" r="14" fill="none" stroke="var(--navy)" stroke-width="1.4"/><rect x="9" y="8" width="12" height="14" rx="1" fill="none" stroke="var(--blue)" stroke-width="1.4"/><path d="M11 12 H19 M11 15 H19 M11 18 H19" stroke="var(--blue)" stroke-width="1.2"/></svg>
      <div>
        <div class="service-name">DATA PROTECTION</div>
        <p class="service-text">We offer cost effective ways to keep your information backed up securely. We check that backups run properly and monitor them on a daily basis.</p>
      </div>
    </div>
    <div class="abs service-item" style="top:268px">
      <svg class="service-icon" viewBox="0 0 30 30"><circle cx="15" cy="15" r="14" fill="none" stroke="var(--navy)" stroke-width="1.4"/><circle cx="12" cy="13" r="3.5" fill="none" stroke="var(--blue)" stroke-width="1.4"/><circle cx="18.5" cy="18" r="3" fill="none" stroke="var(--blue)" stroke-width="1.4"/></svg>
      <div>
        <div class="service-name">IT PROJECTS</div>
        <p class="service-text">We plan, manage and carry out all your technology projects. We promise to meet your goals, on time and on budget.</p>
      </div>
    </div>

    <p class="abs promise-box">We pride ourselves in delivering services that raise your productivity, helping your business run more efficiently and effectively. We are your IT department.</p>
  </div>

  <!-- right page -->
  <div class="page page-right">
    <div class="abs plans-band"></div>
    <h2 class="abs plans-title">STEADYCARE&trade; SERVICE PLANS</h2>
    <p class="abs plans-intro">SERVICE PLANS Keeping your technology safe and up-to-date is not a one-time job. Our SteadyCARE&trade; service plans bring peace of mind for all your data and infrastructure at a fair price. Knowing your computers are safe and maintained saves you stress, letting you focus on what you do best. We offer plans that secure your workstation, tune your servers and network, and keep your data safe.</p>

    <div class="abs plan-card" style="left:46px">
      <svg class="plan-badge" viewBox="0 0 40 40"><circle cx="20" cy="20" r="19" fill="var(--white)" stroke="var(--navy)" stroke-width="2"/><rect x="12" y="13" width="16" height="10" fill="none" stroke="var(--navy)" stroke-width="1.6"/><path d="M10 26 H30" stroke="var(--navy)" stroke-width="1.6"/></svg>
      <div class="plan-name">STEADYCARE&trade;<br>WORKSTATION</div>
      <div class="plan-text">
        <p>You don't have time to keep up with every anti-virus or system update, but you can't afford to skip them. Our Workstation plan delivers enterprise class anti-virus, patching and alerts.</p>
        <p>It's watched 24/7 by our support centre. Rest easy while we keep your computers secure.</p>
      </div>
    </div>
    <div class="abs plan-card" style="left:207px">
      <svg class="plan-badge" viewBox="0 0 40 40"><circle cx="20" cy="20" r="19" fill="var(--white)" stroke="var(--navy)" stroke-width="2"/><rect x="13" y="11" width="9" height="17" fill="none" stroke="var(--navy)" stroke-width="1.6"/><rect x="20" y="16" width="8" height="10" fill="var(--navy)"/></svg>
      <div class="plan-name">STEADYCARE&trade;<br>INFRASTRUCTURE</div>
      <div class="plan-text">
        <p>Our Infrastructure plan makes sure your servers and other key network devices run at peak performance. This includes regular maintenance tasks, monitoring and alerting.</p>
        <p>Because we know your IT setup, we can quickly handle any issue that comes up, cutting your recovery time.</p>
      </div>
    </div>
    <div class="abs plan-card" style="left:368px">
      <svg class="plan-badge" viewBox="0 0 40 40"><circle cx="20" cy="20" r="19" fill="var(--white)" stroke="var(--navy)" stroke-width="2"/><path d="M12 24 Q9 24 10 20 Q11 17 14 18 Q15 13 20 13 Q25 13 26 17 Q30 17 30 21 Q30 24 27 24 Z" fill="none" stroke="var(--navy)" stroke-width="1.6"/></svg>
      <div class="plan-name">STEADYCARE&trade;<br>DATA PROTECTION</div>
      <div class="plan-text">
        <p>When was the last time you ran a full backup and tested that it restores? Our Data Protection plan means we watch your backups daily.</p>
        <p>Problems are flagged to us, we find the cause and fix it so the next backup runs well. You keep a clean, current copy of your data, with regular test restores.</p>
      </div>
    </div>

    <p class="abs rates-note">Rates vary based on your needs. Please contact us for pricing.</p>
  </div>
  <div class="abs fold"></div>
</section>

<!-- BACK COVER -->
<section class="sheet cover-back" aria-label="Back cover">
  <svg class="layer" width="960" height="742" viewBox="0 0 960 742">
    <polygon points="560,0 960,0 960,330" fill="var(--blue)"/>
    <polygon points="830,478 870,478 900,508 860,508" fill="#c9d0d6"/>
    <rect x="330" y="506" width="540" height="2" fill="#3a4856"/>
  </svg>

  <div class="abs brand"><span class="brand-dot"></span>NORTAVEX</div>
  <h2 class="abs back-headline">LEAVE IT TO THE PROFESSIONALS.</h2>
  <p class="abs back-tagline">NORTAVEX is an IT service company providing technology solutions to Calgary<br>and the surrounding area.</p>

  <div class="abs contact-row">
    <span class="contact-item">
      <svg class="contact-icon" viewBox="0 0 16 16"><circle cx="8" cy="8" r="7.5" fill="var(--blue)"/><path d="M5.5 4.5 L7 4.5 L7.5 6.5 L6.6 7.2 Q7.5 9 8.8 9.4 L9.5 8.5 L11.5 9 L11.5 10.5 Q8 11.5 5.5 7 Z" fill="#fff"/></svg>
      555.210.4471
    </span>
    <span class="contact-item">
      <svg class="contact-icon" viewBox="0 0 16 16"><circle cx="8" cy="8" r="7.5" fill="var(--blue)"/><circle cx="8" cy="8" r="4" fill="none" stroke="#fff" stroke-width="1"/><path d="M4 8 H12 M8 4 Q5.8 8 8 12 M8 4 Q10.2 8 8 12" fill="none" stroke="#fff" stroke-width=".8"/></svg>
      www.nortavex.com
    </span>
  </div>

  <div class="abs back-strip">
    <span class="contact-item">
      <svg class="contact-icon" viewBox="0 0 16 16"><circle cx="8" cy="8" r="7.5" fill="var(--navy)"/><rect x="4" y="5.5" width="8" height="5.5" fill="none" stroke="#fff" stroke-width="1"/><path d="M4 5.5 L8 8.5 L12 5.5" fill="none" stroke="#fff" stroke-width="1"/></svg>
      hello@nortavex.com
    </span>
  </div>
</section>

</body>
</html>
```